Life Coaching Business Card

Please check out my website at www.lorettavisbeck.com. Ideally I would like to use the same colors that I used on the site to match my business cards i.e: pink, green, teal, white
I want the final design to include a picture of me and also to be appealing and eye catching. For the picture I submitted, you can crop it smaller to just have my face (exclude my chest) showing.
Industry/Entity Type
Business
Contact Information for Business Card
Loretta Visbeck
Transformational Life Coach
web: www.lorettavisbeck.com
email: loretta@lorettavisbeck.com
Phone: 555-318-7042
Look and feel
Each slider illustrates characteristics of the customer's brand and the style your logo design should communicate.

```html
<!DOCTYPE html>
<html lang="en">
<head>
<meta charset="utf-8">
<title>Loretta Visbeck – Business Card</title>
<link rel="stylesheet" href="https://fonts.googleapis.com/css2?family=Zilla+Slab:wght@300;400&display=swap">
<style>
  :root {
    --paper: #ffffff;
    --pink: #e8228c;
    --green: #b2d235;
    --ink: #111111;
    --text-light: #ffffff;
    --photo-dark: #2a2a2a;
    --photo-light: #d8d8d8;
  }
  html, body {
    margin: 0;
    padding: 0;
    width: 1200px;
    height: 702px;
    overflow: hidden;
    background: var(--paper);
  }
  .card {
    position: relative;
    width: 1200px;
    height: 702px;
    background: var(--paper);
    font-family: "Zilla Slab", Georgia, serif;
  }
  .shadows {
    position: absolute;
    inset: 0;
  }
  .pink-band {
    position: absolute;
    left: 75px;
    top: 0;
    width: 1125px;
    height: 619px;
    background: var(--pink);
  }
  .green-panel {
    position: absolute;
    left: 158px;
    top: 0;
    width: 1042px;
    height: 431px;
    background: var(--green);
  }
  .portrait {
    position: absolute;
    left: 802px;
    top: 41px;
    width: 348px;
    height: 348px;
    background: linear-gradient(135deg, var(--photo-dark) 0%, #6a6a6a 45%, var(--photo-light) 70%, #3a3a3a 100%);
  }
  .name {
    position: absolute;
    right: 426px;
    top: 176px;
    margin: 0;
    font-weight: 300;
    font-size: 96px;
    line-height: 111px;
    color: var(--ink);
    text-align: right;
    letter-spacing: 1px;
  }
  .contact {
    position: absolute;
    left: 101px;
    top: 450px;
    margin: 0;
    padding: 0;
    list-style: none;
    font-weight: 300;
    font-size: 45px;
    line-height: 55px;
    color: var(--text-light);
  }
</style>
</head>
<body>
  <div class="card">
    <svg class="shadows" width="1200" height="702" viewBox="0 0 1200 702" aria-hidden="true">
      <defs>
        <filter id="soft-blur" x="-20%" y="-50%" width="140%" height="200%">
          <feGaussianBlur stdDeviation="10"/>
        </filter>
      </defs>
      <path d="M80 610 Q 110 690 300 680 Q 700 650 1200 640 L1200 615 L80 615 Z" fill="#000" opacity="0.35" filter="url(#soft-blur)"/>
    </svg>

    <div class="pink-band"></div>

    <svg class="shadows" width="1200" height="702" viewBox="0 0 1200 702" aria-hidden="true">
      <path d="M160 425 Q 180 470 420 452 Q 800 428 1200 445 L1200 425 Z" fill="#000" opacity="0.45" filter="url(#soft-blur)"/>
    </svg>

    <div class="green-panel"></div>

    <div class="portrait" role="img" aria-label="Black and white head-and-shoulders portrait of Loretta Visbeck"></div>

    <h1 class="name">Loretta<br>Visbeck</h1>

    <ul class="contact">
      <li class="contact-web">www.lorettavisbeck.com</li>
      <li class="contact-email">email: loretta@lorettavisbeck.com</li>
      <li class="contact-phone">Phone: 555-318-7042</li>
    </ul>
  </div>
</body>
</html>
```